New Meal Prep Flyer for New Package Deals

We are looking for a design that displays our new packages that we offer. If you take a look at our website www.brambleforkmeals.com, and click on packages , you'll see the way we display them currently . We would like something similar to that in style . The first package is called "Horizon" and this package will be a 1 week package (7 days ), 2 meals a day, for a price of $195.00. The second package is called "Amber" and this package will be a 3 week package (21 days) 2 meals per day, for a price of $546.00 , the third package is a 6 week+ package (45 days), and it is called "Evergreen" , 2 meals per day , and the price is $1080.00 .
For the Amber Package , can you put next to it "Save $42.00!"
For the Evergreen Package, can you put next to it "Save $180!"
We also want our logo on the flyer (see attached), and we are just looking for a 1 page flyer , 8 1/2 x 11.

```html
<!DOCTYPE html>
<html lang="en">
<head>
<meta charset="utf-8">
<title>Bramblefork Meal Prep Packages Flyer</title>
<link rel="stylesheet" href="https://fonts.googleapis.com/css2?family=Bebas+Neue&family=Old+Standard+TT:wght@700&family=Roboto:wght@400;500;700&family=Arvo:wght@400;700&display=swap">
<style>
  :root {
    --green: #8dc03f;
    --green-dark: #5f8d26;
    --ink: #3a3a3a;
    --grey: #8f8f8f;
    --tag: #9b9b9b;
    --page-bg: #e4e6e7;
    --white: #ffffff;
    --hero-dark: #2b2a22;
  }
  * { box-sizing: border-box; margin: 0; padding: 0; }
  html, body { width: 1200px; height: 1200px; overflow: hidden; }
  body { background: var(--page-bg); font-family: 'Roboto', Arial, sans-serif; position: relative; }

  .flyer {
    position: absolute; left: 165px; top: 41px;
    width: 870px; height: 1118px;
    background: var(--white); overflow: hidden;
  }

  /* Hero */
  .hero-photo {
    position: absolute; left: 0; top: 0; width: 870px; height: 440px;
    background:
      radial-gradient(ellipse at 30% 30%, rgba(90,120,60,.55), transparent 60%),
      radial-gradient(ellipse at 80% 70%, rgba(150,80,40,.55), transparent 55%),
      linear-gradient(135deg, #3b4a2c 0%, #4a3a2a 45%, #6b4a30 75%, #3a2e22 100%);
  }
  .hero-shade { position: absolute; left: 0; top: 0; width: 870px; height: 440px;
    background: linear-gradient(90deg, rgba(20,20,15,.55), rgba(20,20,15,.15)); }
  .scallop {
    position: absolute; left: 0; top: 423px; width: 870px; height: 20px;
    background: radial-gradient(circle 10px at 16px 10px, var(--white) 98%, transparent 100%) 0 0 / 33px 20px repeat-x;
  }

  .brand { position: absolute; left: 49px; top: 68px; }
  .brand-name { font-family: 'Roboto', sans-serif; font-weight: 700; font-size: 35px; letter-spacing: 2px; color: var(--white); line-height: 1; }
  .brand-tag { margin-top: 6px; font-weight: 700; font-size: 13px; color: var(--green); letter-spacing: .2px; }

  .hero-kicker { position: absolute; left: 49px; top: 160px; font-family: 'Old Standard TT', serif; font-size: 21px; color: var(--white); letter-spacing: .5px; }
  .hero-title { position: absolute; left: 46px; top: 186px; font-family: 'Bebas Neue', sans-serif; font-size: 90px; line-height: 1; color: var(--green); letter-spacing: 0; }
  .hero-sub { position: absolute; left: 49px; top: 266px; font-family: 'Bebas Neue', sans-serif; font-size: 40px; line-height: 1; color: var(--white); }

  .store-badge { position: absolute; top: 347px; height: 39px; border-radius: 4px; }
  .store-badge--light { left: 49px; width: 132px; background: var(--white); }
  .store-badge--dark { left: 200px; width: 124px; background: #111; border: 1px solid #aaa; }

  /* Phone */
  .phone { position: absolute; left: 618px; top: 109px; width: 186px; height: 353px;
    background: #1c1c1c; border: 4px solid #f2f3ea; border-radius: 26px; padding: 9px; }
  .phone-shadow { position: absolute; left: 600px; top: 462px; width: 245px; height: 8px; border-radius: 50%; background: rgba(0,0,0,.25); filter: blur(3px); }
  .phone-screen { position: relative; width: 100%; height: 100%; border-radius: 18px; overflow: hidden;
    background: linear-gradient(180deg, #7a4a2a 0%, #2b2b2b 30%, #3a3226 55%, #8a6a3a 80%, #6a4020 100%); }
  .phone-notch { position: absolute; left: 50%; top: 0; transform: translateX(-50%); width: 80px; height: 12px; background: #1c1c1c; border-radius: 0 0 10px 10px; }
  .screen-brand { position: absolute; top: 62px; width: 100%; text-align: center; font-weight: 700; font-size: 15px; color: var(--white); letter-spacing: 1px; }
  .screen-tag { position: absolute; top: 80px; width: 100%; text-align: center; font-size: 5px; font-weight: 700; color: var(--green); }
  .screen-welcome { position: absolute; top: 96px; width: 100%; text-align: center; font-size: 7px; font-weight: 700; color: var(--white); }
  .screen-copy { position: absolute; top: 115px; left: 10px; right: 10px; text-align: center; font-size: 6px; line-height: 1.4; font-weight: 700; color: var(--white); }
  .screen-btn { position: absolute; top: 266px; width: 66px; height: 18px; border-radius: 4px; font-size: 5px; line-height: 18px; text-align: center; }
  .screen-btn--primary { left: 10px; background: var(--green); color: var(--white); }
  .screen-btn--secondary { right: 10px; background: var(--white); color: #333; }
  .screen-guest { position: absolute; top: 292px; width: 100%; text-align: center; font-size: 5px; color: var(--white); text-decoration: underline; }
  .screen-home { position: absolute; bottom: 6px; left: 50%; transform: translateX(-50%); width: 56px; height: 2px; background: var(--white); border-radius: 2px; }

  /* Intro */
  .intro-line { position: absolute; top: 476px; width: 100%; text-align: center; font-size: 26px; font-weight: 500; color: var(--ink); }
  .intro-cta { position: absolute; top: 518px; width: 100%; text-align: center; font-size: 21px; font-weight: 500; color: var(--green); }

  /* Packages */
  .package { position: absolute; left: 64px; width: 743px; height: 101px;
    border: 2px dotted #333; border-radius: 0 14px 14px 14px; }
  .package--horizon { top: 581px; }
  .package--amber { top: 731px; }
  .package--evergreen { top: 876px; }

  .package-ribbon { position: absolute; left: -19px; top: 28px; height: 42px; background: var(--green);
    color: var(--white); font-weight: 700; font-size: 24px; line-height: 42px; padding-left: 36px; }
  .package-ribbon::before { content: ""; position: absolute; left: 0; top: -8px; border-left: 0 solid transparent;
    border-right: 16px solid transparent; border-bottom: 8px solid var(--green-dark); }
  .package--horizon .package-ribbon, .package--evergreen .package-ribbon { width: 182px; }
  .package--amber .package-ribbon { width: 131px; }

  .package-detail { position: absolute; left: 212px; top: 28px; font-size: 16.5px; line-height: 20px; color: var(--ink); }
  .package-divider { position: absolute; left: 473px; top: 12px; width: 2px; height: 75px; background: linear-gradient(90deg, #ccc, #fff); }

  .package-price { position: absolute; right: 30px; top: 13px; text-align: right; font-family: 'Arvo', serif; }
  .price-label { font-size: 16px; color: var(--grey); font-weight: 700; }
  .price-amount { color: var(--green); font-weight: 700; font-size: 34px; line-height: 1.05; }
  .price-amount .of { font-size: 16px; margin-right: 8px; }
  .price-amount .currency { font-size: 18px; vertical-align: 14px; margin-right: 2px; }

  .save-tag { position: absolute; right: 10px; bottom: -17px; width: 153px; height: 29px; background: var(--tag);
    color: var(--white); font-family: 'Arvo', serif; font-weight: 700; font-size: 16px; line-height: 29px; text-align: center;
    clip-path: polygon(0 0, 100% 0, 96% 50%, 100% 100%, 0 100%, 4% 50%); }

  /* Decorations */
  .deco { position: absolute; border-radius: 50%; background: #f1f1f1; border: 1px solid #d8d8d8; }
  .deco--plate-left { left: -40px; top: 815px; width: 88px; height: 88px; }
  .deco--plate-right { left: 794px; top: 1003px; width: 90px; height: 90px; }
  .deco--spoon { left: 48px; top: 1010px; width: 90px; height: 28px; border-radius: 14px; transform: rotate(40deg); }

  /* Footer */
  .footer { position: absolute; left: 0; top: 1039px; width: 870px; height: 79px; background: var(--green);
    text-align: center; line-height: 60px; font-size: 22px; letter-spacing: 3px; color: var(--white); }
</style>
</head>
<body>
  <main class="flyer">
    <div class="hero-photo" role="img" aria-label="Close-up photograph of healthy meal prep bowls with greens, grains and roasted vegetables"></div>
    <div class="hero-shade"></div>
    <div class="scallop"></div>

    <div class="brand">
      <div class="brand-name">BRAMBLEFORK</div>
      <div class="brand-tag">HEALTHY KITCHEN | MEAL PREP</div>
    </div>

    <p class="hero-kicker">BRAMBLEFORK KITCHEN DELIVERY</p>
    <h1 class="hero-title">YOUR FAVOURITES</h1>
    <p class="hero-sub">DELIVERED TO YOUR DOORSTEP</p>

    <div class="store-badge store-badge--light" role="img" aria-label="App store listing badge"></div>
    <div class="store-badge store-badge--dark" role="img" aria-label="App store listing badge"></div>

    <div class="phone-shadow"></div>
    <div class="phone">
      <div class="phone-screen" role="img" aria-label="App welcome screen over a photo of meal prep containers">
        <div class="phone-notch"></div>
        <div class="screen-brand">BRAMBLEFORK</div>
        <div class="screen-tag">HEALTHY KITCHEN | MEAL PREP</div>
        <div class="screen-welcome">Welcome to the Bramblefork App</div>
        <div class="screen-copy">Earn rewards , review previous order history , order meal prep packages, delivery or take out, and more, all on one app!</div>
        <div class="screen-btn screen-btn--primary">Sign In</div>
        <div class="screen-btn screen-btn--secondary">Register</div>
        <div class="screen-guest">Continue as Guest</div>
        <div class="screen-home"></div>
      </div>
    </div>

    <p class="intro-line">Use the value of your package toward take out or meal</p>
    <p class="intro-cta">Start earning your rewards now!</p>

    <section class="package package--horizon">
      <div class="package-ribbon">Horizon</div>
      <p class="package-detail">1 week package (7 days ),<br>2 meals a day,</p>
      <div class="package-divider"></div>
      <div class="package-price">
        <div class="price-label">for a price</div>
        <div class="price-amount"><span class="of">of</span><span class="currency">$</span>195.00</div>
      </div>
    </section>

    <section class="package package--amber">
      <div class="package-ribbon">Amber</div>
      <p class="package-detail">3 week package (21 days)<br>2 meals per day</p>
      <div class="package-divider"></div>
      <div class="package-price">
        <div class="price-label">for a price</div>
        <div class="price-amount"><span class="of">of</span><span class="currency">$</span>546.00</div>
      </div>
      <div class="save-tag">Save $42.00!</div>
    </section>

    <section class="package package--evergreen">
      <div class="package-ribbon">Evergreen</div>
      <p class="package-detail">6 week+ package (45 days),<br>2 meals per day</p>
      <div class="package-divider"></div>
      <div class="package-price">
        <div class="price-label">for a price</div>
        <div class="price-amount"><span class="of">of</span><span class="currency">$</span>1080.00</div>
      </div>
      <div class="save-tag">Save $180!</div>
    </section>

    <div class="deco deco--plate-left" role="img" aria-label="Line drawing of a plate of food"></div>
    <div class="deco deco--spoon" role="img" aria-label="Line drawing of a spoon"></div>
    <div class="deco deco--plate-right" role="img" aria-label="Line drawing of a breakfast plate"></div>

    <footer class="footer">www.brambleforkmeals.com</footer>
  </main>
</body>
</html>
```